Consulting Business Needs a Cover Designed for a New Book

I need a cover for a book that I am going to self-publish that will be called Summit Sprint. Ways To Sharpen Every Plant Routine And Swiftly Free Up Working Capital. The audience is manufacturing companies. I am looking for something that includes something "extreme" in the cover design, such as wing suits, cliff climbing, etc.

Business

```html
<!DOCTYPE html>
<html lang="en">
<head>
<meta charset="utf-8">
<title>Summit Sprint — Book Cover</title>
<link href="https://fonts.googleapis.com/css2?family=Arimo:wght@400;700&family=Tinos&display=swap" rel="stylesheet">
<style>
  :root {
    --stage: #e6e6ea;
    --cover-dark: #0c0a09;
    --ink-light: #ffffff;
    --author: #d9d1c9;
    --rule: #cfcfd3;
  }
  html, body {
    margin: 0;
    width: 1200px;
    height: 1200px;
    overflow: hidden;
    background: var(--stage);
  }
  .book-cover {
    position: absolute;
    left: 185px;
    top: 30px;
    width: 829px;
    height: 1140px;
    background: var(--cover-dark);
    overflow: hidden;
  }
  .cover-art {
    position: absolute;
    inset: 0;
    width: 100%;
    height: 100%;
  }
  .title {
    position: absolute;
    left: 104px;
    top: 78px;
    margin: 0;
    font-family: "Arimo", Arial, sans-serif;
    font-weight: 400;
    font-size: 72px;
    line-height: 1;
    letter-spacing: -1px;
    color: var(--cover-dark);
    -webkit-text-stroke: 2px var(--ink-light);
    white-space: nowrap;
  }
  .title .title-accent {
    font-weight: 700;
    font-size: 98px;
    color: var(--ink-light);
    -webkit-text-stroke: 0;
  }
  .subtitle {
    position: absolute;
    left: 104px;
    top: 174px;
    margin: 0;
    font-family: "Arimo", Arial, sans-serif;
    color: var(--ink-light);
    white-space: nowrap;
  }
  .subtitle-lead {
    display: block;
    font-weight: 400;
    font-size: 24px;
    line-height: 40px;
  }
  .subtitle-line {
    display: block;
    font-weight: 700;
    font-size: 24px;
    line-height: 42px;
  }
  .author {
    position: absolute;
    left: 0;
    right: 0;
    top: 1052px;
    text-align: center;
    font-family: "Tinos", "Times New Roman", serif;
    font-size: 27px;
    letter-spacing: 0.5px;
    color: var(--author);
  }
</style>
</head>
<body>
  <div class="book-cover">
    <svg class="cover-art" viewBox="0 0 958 1318" preserveAspectRatio="none" role="img" aria-label="Photograph of a rock climber hanging from a cliff face above desert mountain spires, seen through diagonal rounded bands">
      <defs>
        <radialGradient id="backdropGlow" cx="0.45" cy="0.78" r="0.6">
          <stop offset="0" stop-color="#6b3a26"/>
          <stop offset="0.55" stop-color="#2a1710"/>
          <stop offset="1" stop-color="#0c0a09"/>
        </radialGradient>
        <linearGradient id="bandFill" gradientUnits="userSpaceOnUse" x1="0" y1="0" x2="0" y2="1100">
          <stop offset="0" stop-color="#a8772f"/>
          <stop offset="0.3" stop-color="#d9b57c"/>
          <stop offset="0.5" stop-color="#f4ece1"/>
          <stop offset="0.72" stop-color="#cda592"/>
          <stop offset="0.9" stop-color="#e8e2e2"/>
          <stop offset="1" stop-color="#d7d0d2"/>
        </linearGradient>
        <linearGradient id="cliffShade" x1="0" y1="0" x2="1" y2="0">
          <stop offset="0" stop-color="#000" stop-opacity="0"/>
          <stop offset="0.7" stop-color="#000" stop-opacity="0"/>
          <stop offset="1" stop-color="#140f0c" stop-opacity="0.85"/>
        </linearGradient>
        <clipPath id="coverClip">
          <rect x="0" y="0" width="958" height="1288"/>
        </clipPath>
      </defs>

      <rect class="backdrop" x="0" y="0" width="958" height="1318" fill="url(#backdropGlow)"/>

      <g class="diagonal-bands" clip-path="url(#coverClip)" fill="url(#bandFill)" opacity="0.93">
        <rect x="12" y="422" width="1500" height="176" rx="88" transform="rotate(-45 100 510)"/>
        <rect x="17" y="682" width="1500" height="176" rx="88" transform="rotate(-45 105 770)"/>
        <rect x="62" y="922" width="1500" height="176" rx="88" transform="rotate(-45 150 1010)"/>
        <rect x="352" y="912" width="1500" height="176" rx="88" transform="rotate(-45 440 1000)"/>
        <rect x="667" y="877" width="1500" height="176" rx="88" transform="rotate(-45 755 965)"/>
      </g>

      <rect class="cliff-shade" x="0" y="0" width="958" height="1288" fill="url(#cliffShade)"/>

      <rect class="base-rule" x="0" y="1288" width="958" height="6" fill="var(--rule)"/>
      <rect class="base-band" x="0" y="1294" width="958" height="24" fill="#141416"/>
    </svg>

    <h1 class="title">S<span class="title-accent">U</span>MMIT SPRINT</h1>

    <p class="subtitle">
      <span class="subtitle-lead">WAYS TO</span>
      <span class="subtitle-line">SHARPEN EVERY PLANT ROUTINE AND</span>
      <span class="subtitle-line">SWIFTLY FREE UP WORKING CAPITAL</span>
    </p>

    <div class="author">AUTHOR NAME</div>
  </div>
</body>
</html>
```